Harlowe Skid Service Business Cards

WHAT WE DOWe RepairWe CustomizeWe ManufactureWe Deliver
Reason: Hello,
I would like to extend the deadline to May 1st - no additional fee. Reason being is because I am waiting on a reply from feedback from the designed that we are planning on choosing. I would like an answer as soon as possible, please and thanks!!!
Industry/Entity Type
Business
Contact Information for Business Card
Mireya Quintanal
Vice President
Office: 847-555-0142
Cell: 708-555-0187
Fax: 847-555-0163
mireya@harloweskid.com
Harlowe Skid Service II, Inc
2290 Fernhollow Avenue
Marlow Ridge, IL 60099
www.harloweskid.com
Look and feel
Each slider illustrates characteristics of the customer's brand and the style your logo design should communicate.

```html
<!DOCTYPE html>
<html lang="en">
<head>
<meta charset="utf-8">
<title>Harlowe Skid Service – Business Cards</title>
<link rel="stylesheet" href="https://fonts.googleapis.com/css2?family=Lato:wght@300;400;700;900&display=swap">
<style>
  :root {
    --maroon: #441417;
    --gold: #f2c77a;
    --gold-line: #e9c58a;
    --ink: #2a1214;
    --ink-soft: #3b2b2c;
    --muted: #8b8385;
    --paper: #ffffff;
    --stage: #d3d3d3;
    --machine-orange: #f0a230;
    --grass: #8aa04a;
  }
  * { box-sizing: border-box; margin: 0; padding: 0; }
  html, body { width: 1200px; height: 1200px; overflow: hidden; }
  body {
    background: var(--stage);
    font-family: "Lato", sans-serif;
    color: var(--ink-soft);
    position: relative;
  }
  .card {
    position: absolute;
    left: 150px;
    width: 900px;
    height: 514px;
    overflow: hidden;
    box-shadow: 0 6px 18px rgba(0,0,0,.18);
  }
  .card--front { top: 52px; background: var(--paper); }
  .card--back { top: 624px; background: var(--maroon); }

  .card__wave { position: absolute; inset: 0; width: 100%; height: 100%; }

  .illustration {
    position: absolute;
    border-radius: 10px;
    background: linear-gradient(160deg, #3a3a3a 0%, var(--machine-orange) 55%, #d9b98a 75%, var(--grass) 100%);
  }
  .card--front .illustration { right: 50px; top: 36px; width: 300px; height: 230px; }
  .card--back .illustration { left: 300px; top: 132px; width: 300px; height: 250px; }

  .identity { position: absolute; left: 62px; top: 74px; }
  .identity__name { font-size: 40px; font-weight: 900; color: var(--ink); letter-spacing: .3px; }
  .identity__title { font-size: 21px; font-weight: 300; color: var(--muted); margin-top: 2px; }

  .company { position: absolute; left: 62px; top: 172px; line-height: 1.3; }
  .company__name { font-size: 24px; font-weight: 400; color: var(--gold); }
  .company__address { font-size: 22px; font-weight: 400; color: var(--ink-soft); }

  .contacts { position: absolute; left: 62px; top: 292px; list-style: none; }
  .contacts__item {
    display: flex; align-items: center; gap: 22px;
    font-size: 22px; font-weight: 400; color: var(--ink-soft);
    height: 37px;
  }
  .contacts__icon { width: 22px; height: 22px; flex: none; fill: var(--maroon); }
</style>
</head>
<body>

  <section class="card card--front" aria-label="Business card front">
    <svg class="card__wave" viewBox="0 0 900 514" preserveAspectRatio="none" aria-hidden="true">
      <path d="M300 514 C 520 505, 610 400, 690 320 S 840 210 900 200 L900 514 Z" fill="var(--maroon)"/>
      <path d="M290 514 C 515 500, 600 392, 684 312 S 838 202 900 192" fill="none" stroke="var(--gold-line)" stroke-width="4"/>
    </svg>

    <div class="illustration" role="img" aria-label="Illustration of a worker driving an orange forklift carrying boxes on a pallet"></div>

    <header class="identity">
      <h1 class="identity__name">Mireya Quintanal</h1>
      <p class="identity__title">Vice President</p>
    </header>

    <div class="company">
      <p class="company__name">Harlowe Skid Service II, Inc</p>
      <p class="company__address">2290 Fernhollow Avenue</p>
      <p class="company__address">Marlow Ridge, IL 60099</p>
    </div>

    <ul class="contacts">
      <li class="contacts__item">
        <svg class="contacts__icon" viewBox="0 0 24 24" aria-label="Office"><path d="M3 8c0-2 3-4 9-4s9 2 9 4v2h-5V8H8v2H3z"/><rect x="5" y="12" width="14" height="8" rx="2"/></svg>
        847-555-0142
      </li>
      <li class="contacts__item">
        <svg class="contacts__icon" viewBox="0 0 24 24" aria-label="Cell"><path d="M7 2h10a1 1 0 0 1 1 1v18a1 1 0 0 1-1 1H7a1 1 0 0 1-1-1V3a1 1 0 0 1 1-1zm1 3v13h8V5z"/></svg>
        708-555-0187
      </li>
      <li class="contacts__item">
        <svg class="contacts__icon" viewBox="0 0 24 24" aria-label="Fax"><path d="M7 3h8l3 3v4H7z"/><rect x="3" y="11" width="18" height="9" rx="1.5"/><rect x="6" y="14" width="8" height="2" fill="#fff"/></svg>
        847-555-0163
      </li>
      <li class="contacts__item">
        <svg class="contacts__icon" viewBox="0 0 24 24" aria-label="Email"><path d="M2 5h20v14H2z"/><path d="M2 5l10 8 10-8" fill="none" stroke="#fff" stroke-width="1.6"/></svg>
        mireya@harloweskid.com
      </li>
      <li class="contacts__item">
        <svg class="contacts__icon" viewBox="0 0 24 24" aria-label="Website"><circle cx="12" cy="12" r="10"/><path d="M2 12h20M12 2c3 3 3 17 0 20M12 2c-3 3-3 17 0 20" fill="none" stroke="#fff" stroke-width="1.3"/></svg>
        www.harloweskid.com
      </li>
    </ul>
  </section>

  <section class="card card--back" aria-label="Business card back">
    <div class="illustration" role="img" aria-label="Illustration of a worker driving an orange forklift carrying boxes on a pallet"></div>
  </section>

</body>
</html>
```